a graphic model of stress response for online learning course

We need a model of how the brain experiences, interprets and responds to stressors. There are three components to this.

I need a simple linear graphic of the three stages with arrows between to show progression:
1. We experience the stressor
2. Our brain interprets the stressor: Is it a threat? Is it friendly?
3. Our brain creates the appropriate stress response: physical, mental, emotional

And another graphic with illustrations of this process:
A charging lion
A brain thinking/interpreting the potential stressor
A person running away (the response to the threat).

Needs to be used for online learning course about stress and resilience.

See attached for assistance.

```html
<!DOCTYPE html>
<html lang="en">
<head>
<meta charset="utf-8">
<title>Stress Response Model</title>
<link rel="stylesheet" href="https://fonts.googleapis.com/css2?family=Montserrat:wght@700;800&display=swap">
<style>
  :root {
    --bg: #ffffff;
    --ink: #2b2b2b;
    --orange-light: #fc9155;
    --orange-dark: #f57422;
    --grey-light: #b8b8b8;
    --grey-dark: #9b9b9b;
    --yellow-light: #fdd443;
    --yellow-dark: #f5c40a;
    --outline: #ffffff;
  }
  html, body {
    margin: 0;
    padding: 0;
    background: var(--bg);
    overflow: hidden;
  }
  .canvas {
    position: relative;
    width: 1200px;
    height: 1000px;
    overflow: hidden;
    background: var(--bg);
    font-family: "Montserrat", Arial, sans-serif;
    color: var(--ink);
  }
  .stages {
    position: absolute;
    inset: 0;
  }
  .stage-number {
    position: absolute;
    width: 70px;
    top: 295px;
    text-align: center;
    font-weight: 800;
    font-size: 33px;
    line-height: 38px;
    letter-spacing: 0.5px;
    color: var(--ink);
  }
  .stage-caption {
    position: absolute;
    top: 552px;
    margin: 0;
    font-weight: 700;
    font-size: 17.5px;
    line-height: 20.5px;
    color: var(--ink);
  }
  .stage-caption--one { left: 103px; top: 555px; }
  .stage-caption--two { left: 449px; }
  .stage-caption--three { left: 794px; }
  .stage-number--one { left: 146px; }
  .stage-number--two { left: 492px; }
  .stage-number--three { left: 838px; }
</style>
</head>
<body>
<main class="canvas">
  <svg class="stages" width="1200" height="1000" viewBox="0 0 1200 1000" aria-hidden="false">
    <defs>
      <linearGradient id="chevron-orange" x1="0" y1="0" x2="0" y2="1">
        <stop offset="0" stop-color="var(--orange-light)"/>
        <stop offset="1" stop-color="var(--orange-dark)"/>
      </linearGradient>
      <linearGradient id="chevron-grey" x1="0" y1="0" x2="0" y2="1">
        <stop offset="0" stop-color="var(--grey-light)"/>
        <stop offset="1" stop-color="var(--grey-dark)"/>
      </linearGradient>
      <linearGradient id="chevron-yellow" x1="0" y1="0" x2="0" y2="1">
        <stop offset="0" stop-color="var(--yellow-light)"/>
        <stop offset="1" stop-color="var(--yellow-dark)"/>
      </linearGradient>
      <linearGradient id="band-orange" x1="0" y1="0" x2="1" y2="0">
        <stop offset="0" stop-color="var(--orange-light)"/>
        <stop offset="1" stop-color="var(--orange-dark)"/>
      </linearGradient>
      <linearGradient id="band-grey" x1="0" y1="0" x2="1" y2="0">
        <stop offset="0" stop-color="var(--grey-light)"/>
        <stop offset="1" stop-color="var(--grey-dark)"/>
      </linearGradient>
      <linearGradient id="band-yellow" x1="0" y1="0" x2="1" y2="0">
        <stop offset="0" stop-color="var(--yellow-light)"/>
        <stop offset="1" stop-color="var(--yellow-dark)"/>
      </linearGradient>
      <linearGradient id="fold-shade" x1="0" y1="0" x2="1" y2="1">
        <stop offset="0" stop-color="#000" stop-opacity="0.22"/>
        <stop offset="1" stop-color="#000" stop-opacity="0"/>
      </linearGradient>
      <filter id="soft-shadow" x="-20%" y="-20%" width="150%" height="150%">
        <feDropShadow dx="8" dy="8" stdDeviation="9" flood-color="#000" flood-opacity="0.22"/>
      </filter>
    </defs>

    <!-- Stage 1 -->
    <g class="stage stage--one">
      <path class="chevron" d="M82 305 H387 L462 438 L387 571 H82 L157 438 Z" fill="url(#chevron-orange)" filter="url(#soft-shadow)"/>
      <path class="fold" d="M143 307 L206 307 L168 395 L113 357 Z" fill="url(#fold-shade)"/>
      <rect class="illustration" role="img" aria-label="Outline illustration of a charging lion" x="156" y="376" width="218" height="156" rx="24" fill="#f7822f"/>
      <path class="caption-band" d="M80 524 H342.5 A55.5 55.5 0 0 1 342.5 635 H80 Z" fill="url(#band-orange)" stroke="var(--outline)" stroke-width="3"/>
      <circle class="badge" cx="181" cy="314" r="35" fill="url(#band-orange)" stroke="var(--outline)" stroke-width="3"/>
    </g>

    <!-- Stage 2 -->
    <g class="stage stage--two">
      <path class="chevron" d="M428 305 H733 L808 438 L733 571 H428 L503 438 Z" fill="url(#chevron-grey)" filter="url(#soft-shadow)"/>
      <path class="fold" d="M489 307 L552 307 L514 395 L459 357 Z" fill="url(#fold-shade)"/>
      <rect class="illustration" role="img" aria-label="Outline illustration of a head in profile with a brain and a question mark" x="531" y="359" width="155" height="164" rx="24" fill="#a9a9a9"/>
      <path class="caption-band" d="M428 524 H690.5 A55.5 55.5 0 0 1 690.5 635 H428 Z" fill="url(#band-grey)" stroke="var(--outline)" stroke-width="3"/>
      <circle class="badge" cx="527" cy="314" r="35" fill="url(#band-grey)" stroke="var(--outline)" stroke-width="3"/>
    </g>

    <!-- Stage 3 -->
    <g class="stage stage--three">
      <path class="chevron" d="M773 305 H1078 L1153 438 L1078 571 H773 L848 438 Z" fill="url(#chevron-yellow)" filter="url(#soft-shadow)"/>
      <path class="fold" d="M834 307 L897 307 L859 395 L804 357 Z" fill="url(#fold-shade)"/>
      <path class="caption-band" d="M773 524 H1035.5 A55.5 55.5 0 0 1 1035.5 635 H773 Z" fill="url(#band-yellow)" stroke="var(--outline)" stroke-width="3"/>
      <rect class="illustration" role="img" aria-label="Outline illustration of a person running away" x="877" y="337" width="157" height="234" rx="24" fill="#f8ca1e"/>
      <circle class="badge" cx="876" cy="314" r="35" fill="url(#band-yellow)" stroke="var(--outline)" stroke-width="3"/>
    </g>
  </svg>

  <span class="stage-number stage-number--one">01</span>
  <span class="stage-number stage-number--two">02</span>
  <span class="stage-number stage-number--three">03</span>

  <p class="stage-caption stage-caption--one">We experience<br>the stressor</p>
  <p class="stage-caption stage-caption--two">Our brain interprets<br>the stressor:<br>Is it a threat? Is it friendly?</p>
  <p class="stage-caption stage-caption--three">Our brain creates the<br>appropriate stress response:<br>physical, mental, emotional</p>
</main>
</body>
</html>
```